Window Tinting

We are a window tinting company for automotive. Our main clientele has been the dealerships but now we are looking to expand to the general public. "Glidra" is actually short for gLidration (versus a measurement of time). We are hoping to make the "X" signature. Something easily noticed for later marketing. Right now since our name is kinda new, we'd rather the card scream "window tinting" versus our name being the main focus.. Window tint is a clean crisp aftermarket addition for vehicles and hopefully the business card can create that same attitude.

Industry/Entity Type

Automotive

Contact Information for Business Card

Glidra Shades Llc Ravi "Doc" Pellham
816 Lindcrest Ave. unit B
North Haven, Ct 06519 203.571.2094

```html
<!DOCTYPE html>
<html lang="en">
<head>
<meta charset="utf-8">
<title>Glidra Shades – Business Card</title>
<link rel="stylesheet" href="https://fonts.googleapis.com/css2?family=Open+Sans:wght@400;600;700&display=swap">
<style>
  :root {
    --tint-red: #dc1f26;
    --card-white: #ffffff;
    --ink-grey: #4a4a4a;
    --backdrop: #9b9b9b;
    --card-shadow: rgba(0, 0, 0, 0.28);
  }
  * { box-sizing: border-box; margin: 0; padding: 0; }
  html, body {
    width: 1200px;
    height: 900px;
    overflow: hidden;
    background: var(--backdrop);
    font-family: "Open Sans", Arial, sans-serif;
  }
  .stage {
    position: relative;
    width: 1200px;
    height: 900px;
  }
  .card {
    position: absolute;
    width: 540px;
    height: 308px;
    background: var(--card-white);
    box-shadow: 0 6px 18px var(--card-shadow);
    overflow: hidden;
  }
  .card--front { left: 600px; top: 110px; }
  .card--back  { left: 80px;  top: 470px; }

  /* Front card bands */
  .front-band-top {
    position: absolute; left: 0; top: 0; width: 100%; height: 58px;
    background: var(--tint-red);
  }
  .front-band-bottom {
    position: absolute; left: 0; bottom: 14px; width: 100%; height: 24px;
    background: var(--tint-red);
  }

  /* Wordmark */
  .wordmark {
    position: absolute;
    display: flex;
    align-items: center;
    gap: 14px;
  }
  .wordmark__name {
    font-weight: 400;
    color: var(--ink-grey);
    letter-spacing: 0.5px;
    line-height: 1;
  }
  .wordmark__mark {
    background: var(--tint-red);
    flex: none;
  }
  .card--front .wordmark {
    left: 50%; top: 118px; transform: translateX(-50%);
  }
  .card--front .wordmark__name { font-size: 44px; }
  .card--front .wordmark__mark { width: 40px; height: 40px; }

  .card--back .wordmark { right: 40px; top: 52px; }
  .card--back .wordmark__name { font-size: 36px; }
  .card--back .wordmark__mark { width: 32px; height: 32px; }

  /* Back card red panel */
  .back-panel {
    position: absolute; left: 0; top: 122px; width: 100%; height: 164px;
    background: var(--tint-red);
    color: var(--card-white);
  }
  .person {
    position: absolute; left: 22px; top: 14px;
  }
  .person__name { font-size: 21px; font-weight: 700; line-height: 1.1; }
  .person__role { font-size: 13px; font-weight: 400; }

  .contacts {
    position: absolute; right: 18px; bottom: 12px;
    list-style: none;
    text-align: right;
  }
  .contacts__item {
    display: flex; justify-content: flex-end; align-items: center;
    gap: 8px;
    font-size: 15px; line-height: 21px;
  }
  .contacts__icon { width: 12px; height: 12px; flex: none; fill: var(--card-white); }
</style>
</head>
<body>
<main class="stage">

  <section class="card card--front" aria-label="Business card front">
    <div class="front-band-top"></div>
    <div class="wordmark">
      <span class="wordmark__name">Glidra Shades</span>
      <span class="wordmark__mark"></span>
    </div>
    <div class="front-band-bottom"></div>
  </section>

  <section class="card card--back" aria-label="Business card back">
    <div class="wordmark">
      <span class="wordmark__name">Glidra Shades</span>
      <span class="wordmark__mark"></span>
    </div>
    <div class="back-panel">
      <div class="person">
        <p class="person__name">Corwin Ashby</p>
        <p class="person__role">Managing Director</p>
      </div>
      <ul class="contacts">
        <li class="contacts__item">555.014.2287
          <svg class="contacts__icon" viewBox="0 0 12 12" aria-hidden="true"><path d="M2.5 1h2l1 2.5-1.2 1a6 6 0 0 0 3.2 3.2l1-1.2L11 7.5v2c0 .8-.7 1.5-1.5 1.5A8.5 8.5 0 0 1 1 2.5C1 1.7 1.7 1 2.5 1z"/></svg>
        </li>
        <li class="contacts__item">555.014.2288
          <svg class="contacts__icon" viewBox="0 0 12 12" aria-hidden="true"><path d="M3.5 0h5A1.5 1.5 0 0 1 10 1.5v9A1.5 1.5 0 0 1 8.5 12h-5A1.5 1.5 0 0 1 2 10.5v-9A1.5 1.5 0 0 1 3.5 0zM3.5 1.5v7.5h5V1.5zM6 9.8a.8.8 0 1 0 0 1.6.8.8 0 0 0 0-1.6z"/></svg>
        </li>
        <li class="contacts__item">hello@glidrashades.com
          <svg class="contacts__icon" viewBox="0 0 12 12" aria-hidden="true"><path d="M0 2.5h12v7H0zM1 3.2l5 3.6 5-3.6v-.1H1z"/></svg>
        </li>
        <li class="contacts__item">www.glidrashades.com
          <svg class="contacts__icon" viewBox="0 0 12 12" aria-hidden="true"><path d="M5 7 7 5M4.5 5.5 3 7a1.8 1.8 0 0 0 2.5 2.5L7 8M7.5 6.5 9 5a1.8 1.8 0 0 0-2.5-2.5L5 4" stroke="#fff" stroke-width="1.4" fill="none" stroke-linecap="round"/></svg>
        </li>
        <li class="contacts__item">88 Larkfield Rd, Northvale, Ct 00412
          <svg class="contacts__icon" viewBox="0 0 12 12" aria-hidden="true"><path d="M6 0a4 4 0 0 1 4 4c0 3-4 8-4 8S2 7 2 4a4 4 0 0 1 4-4zm0 2.3a1.7 1.7 0 1 0 0 3.4 1.7 1.7 0 0 0 0-3.4z"/></svg>
        </li>
      </ul>
    </div>
  </section>

</main>
</body>
</html>
```